Business Card For Kelmora Financial Consulting

Hi, I would like a business card designed. Bold, modern.
Please use the same design as the logo. I have also attached the website design to see the overall theme.
Wordmark Font
Color: Hex: #01AEF7

```html
<!DOCTYPE html>
<html lang="en">
<head>
<meta charset="utf-8">
<title>Kelmora Consulting – Business Card</title>
<link rel="stylesheet" href="https://fonts.googleapis.com/css2?family=Poppins:wght@400;500;700&display=swap">
<style>
  :root{
    --bg:#2b2b2d;
    --navy:#17222e;
    --navy-deep:#0d141c;
    --ink:#123a5c;
    --blue:#01aef7;
    --steel:#3d7fb3;
    --text:#111418;
    --white:#ffffff;
    --rule:#b9bec4;
  }
  *{box-sizing:border-box;margin:0;padding:0}
  html,body{width:1200px;height:689px;overflow:hidden;background:var(--bg)}
  body{font-family:"Poppins",sans-serif;position:relative}

  .card{
    position:absolute;top:190px;width:540px;height:309px;
    border-radius:22px;overflow:hidden;
  }

  /* back of card */
  .card--back{left:40px;background:var(--navy)}
  .card--back .decor{
    position:absolute;left:0;top:0;width:330px;height:309px;
    background:linear-gradient(150deg,var(--steel) 0%,#1d4466 35%,var(--navy-deep) 100%);
    clip-path:polygon(0 0,78% 0,100% 100%,0 100%);
    opacity:.9;
  }
  .card--back .wordmark{
    position:absolute;left:420px;top:154px;
    transform:translate(-50%,-50%) rotate(-90deg);
    text-align:center;white-space:nowrap;
  }
  .wordmark__name,.wordmark__sub{
    display:block;font-weight:700;color:var(--white);
  }
  .card--back .wordmark__name{font-size:40px;letter-spacing:2px;line-height:1}
  .card--back .wordmark__sub{font-size:11px;letter-spacing:12px;margin-top:6px}

  /* front of card */
  .card--front{left:620px;background:var(--white)}
  .card--front .brand{
    position:absolute;left:34px;top:118px;display:flex;align-items:center;gap:10px;
  }
  .brand__mark{width:22px;height:22px;background:var(--blue)}
  .brand__text .wordmark__name,.brand__text .wordmark__sub{color:var(--ink)}
  .brand__text .wordmark__name{font-size:26px;letter-spacing:1px;line-height:1}
  .brand__text .wordmark__sub{font-size:8px;letter-spacing:9px;margin-top:4px}

  .divider{position:absolute;left:262px;top:36px;width:1px;height:190px;background:var(--rule)}

  .contact{position:absolute;left:286px;top:42px;color:var(--text)}
  .contact__name{font-size:19px;font-weight:700;color:var(--ink);line-height:1.1}
  .contact__role{font-size:11px;font-weight:500;color:var(--blue);letter-spacing:.6px;margin-bottom:12px}
  .contact__line{display:flex;align-items:center;gap:8px;font-size:12px;line-height:1.55}
  .contact__line svg{width:12px;height:12px;flex:none}
  .contact__line .accent{color:var(--blue)}
  .contact__address{font-size:12px;line-height:1.35;margin-top:10px}

  .band{position:absolute;left:0;bottom:0;width:100%;height:32px;background:var(--navy)}
  .band__rule{position:absolute;left:0;bottom:38px;width:100%;height:3px;background:var(--blue)}
</style>
</head>
<body>

<section class="card card--back">
  <div class="decor" role="img" aria-label="Abstract angled blue panel decoration"></div>
  <div class="wordmark">
    <span class="wordmark__name">KELMORA</span>
    <span class="wordmark__sub">CONSULTING</span>
  </div>
</section>

<section class="card card--front">
  <div class="brand">
    <span class="brand__mark"></span>
    <div class="brand__text">
      <span class="wordmark__name">KELMORA</span>
      <span class="wordmark__sub">CONSULTING</span>
    </div>
  </div>

  <div class="divider"></div>

  <div class="contact">
    <p class="contact__name">MARCUS HALE</p>
    <p class="contact__role">MANAGING DIRECTOR</p>
    <p class="contact__line">
      <svg viewBox="0 0 24 24" fill="var(--blue)"><path d="M6.6 10.8a15.1 15.1 0 0 0 6.6 6.6l2.2-2.2a1 1 0 0 1 1-.25 11.4 11.4 0 0 0 3.6.57 1 1 0 0 1 1 1V20a1 1 0 0 1-1 1A17 17 0 0 1 3 4a1 1 0 0 1 1-1h3.5a1 1 0 0 1 1 1c0 1.25.2 2.45.57 3.57a1 1 0 0 1-.25 1z"/></svg>
      044-555 018 274
    </p>
    <p class="contact__line">
      <svg viewBox="0 0 24 24" fill="var(--blue)"><path d="M2 5h20v14H2z M2 5l10 8 10-8" stroke="#fff" stroke-width="1.5"/></svg>
      info@kelmora.com
    </p>
    <p class="contact__line">
      <svg viewBox="0 0 24 24" fill="none" stroke="var(--blue)" stroke-width="2"><circle cx="12" cy="12" r="10"/><path d="M2 12h20M12 2c3 3 3 17 0 20M12 2c-3 3-3 17 0 20"/></svg>
      <span>www.<span class="accent">kelmoraconsulting</span>.com</span>
    </p>
    <p class="contact__address">17, Harbour Lane North<br>30218, Westmark</p>
  </div>

  <div class="band__rule"></div>
  <div class="band"></div>
</section>

</body>
</html>
```